Medical software helping patients with dry eye disease needs a business card

We have a logo we just need a design for a business card for a Canadian company called LOV: Dry Eye. We use AI technology to assist optometrists in properly diagnosing patients with dry eye disease reducing wait times in doctors offices and accuracy of diagnosis as well as identifying key possible indicators and tailored treatment plans. The final design should be clean and medical looking. Our mission is to help patients and our logo using blues and whites.

```html
<!DOCTYPE html>
<html lang="en">
<head>
<meta charset="utf-8">
<title>LOV: Dry Eye — Business Card</title>
<link rel="stylesheet" href="https://fonts.googleapis.com/css2?family=Lato:wght@400;700;900&display=swap">
<style>
  :root {
    --backdrop: #2a2b2d;
    --navy: #0f4778;
    --sky: #27a9e1;
    --ink: #1c1f24;
    --paper: #ffffff;
  }
  * { margin: 0; padding: 0; box-sizing: border-box; }
  html, body { width: 1200px; height: 962px; overflow: hidden; }
  body {
    background: var(--backdrop);
    font-family: "Lato", Arial, sans-serif;
    display: flex;
    flex-direction: column;
    align-items: center;
    justify-content: center;
    gap: 40px;
  }
  .card {
    width: 720px;
    height: 411px;
    border-radius: 22px;
    position: relative;
    overflow: hidden;
  }
  .card-front {
    background: var(--navy);
    display: flex;
    align-items: center;
    justify-content: center;
  }
  .wordmark {
    display: flex;
    align-items: center;
    gap: 18px;
  }
  .wordmark-dot {
    border-radius: 50%;
    flex: none;
  }
  .wordmark-name {
    font-weight: 900;
    white-space: nowrap;
    letter-spacing: 0.01em;
  }
  .card-front .wordmark-dot { width: 74px; height: 74px; background: var(--sky); }
  .card-front .wordmark-name { font-size: 64px; color: var(--paper); }

  .card-back {
    background: var(--paper);
    display: flex;
    align-items: center;
  }
  .card-back .brand {
    width: 320px;
    display: flex;
    justify-content: center;
  }
  .card-back .wordmark { gap: 12px; }
  .card-back .wordmark-dot { width: 40px; height: 40px; background: var(--navy); }
  .card-back .wordmark-name { font-size: 34px; color: var(--sky); }
  .divider {
    width: 2px;
    height: 220px;
    background: var(--navy);
    flex: none;
  }
  .contact {
    padding-left: 30px;
  }
  .person-name {
    font-weight: 900;
    font-size: 30px;
    color: var(--navy);
    text-transform: uppercase;
    letter-spacing: 0.01em;
    line-height: 1.1;
  }
  .person-title {
    font-size: 19px;
    color: var(--sky);
    margin-bottom: 16px;
  }
  .contact-list { list-style: none; }
  .contact-item {
    display: flex;
    align-items: flex-start;
    gap: 10px;
    font-size: 17px;
    color: var(--ink);
    line-height: 1.35;
    margin-bottom: 5px;
  }
  .contact-item.phone { font-weight: 700; font-size: 19px; }
  .contact-icon { width: 16px; height: 16px; flex: none; margin-top: 3px; fill: var(--sky); }
</style>
</head>
<body>
  <section class="card card-front">
    <div class="wordmark">
      <span class="wordmark-dot"></span>
      <span class="wordmark-name">LOV: Dry Eye</span>
    </div>
  </section>

  <section class="card card-back">
    <div class="brand">
      <div class="wordmark">
        <span class="wordmark-dot"></span>
        <span class="wordmark-name">LOV: Dry Eye</span>
      </div>
    </div>
    <div class="divider"></div>
    <div class="contact">
      <h1 class="person-name">Daniel Whitford</h1>
      <p class="person-title">Founder &amp; CEO</p>
      <ul class="contact-list">
        <li class="contact-item address">
          <svg class="contact-icon" viewBox="0 0 16 16"><path d="M8 0a5.5 5.5 0 0 0-5.5 5.5C2.5 10 8 16 8 16s5.5-6 5.5-10.5A5.5 5.5 0 0 0 8 0zm0 8a2.5 2.5 0 1 1 0-5 2.5 2.5 0 0 1 0 5z"/></svg>
          <span>220 4410 Maple Ave SW<br>Calgary, AB T3A 1B7</span>
        </li>
        <li class="contact-item phone">
          <svg class="contact-icon" viewBox="0 0 16 16"><path d="M3.6 1l2.2 3-1.3 1.6a9 9 0 0 0 5.9 5.9L12 10.2l3 2.2-1.4 2.6C7.3 15 1 8.7 1 2.4z"/></svg>
          <span>403-555-0147</span>
        </li>
        <li class="contact-item email">
          <svg class="contact-icon" viewBox="0 0 16 16"><path d="M1 3h14v1.2L8 9 1 4.2zm0 2.6l7 4.8 7-4.8V13H1z"/></svg>
          <span>info@lovdryeye.com</span>
        </li>
        <li class="contact-item web">
          <svg class="contact-icon" viewBox="0 0 16 16"><path d="M8 0a8 8 0 1 0 0 16A8 8 0 0 0 8 0zm0 1.5c.9 0 2 1.9 2.4 5H5.6C6 3.4 7.1 1.5 8 1.5zM1.6 7.5h2.5c0 1.1.1 2.1.3 3H2.2a6.4 6.4 0 0 1-.6-3zm.6-1.6A6.5 6.5 0 0 1 5.4 2c-.5 1-.9 2.4-1.1 3.9zm3.4 1.6h4.8c0 1.1-.1 2.1-.3 3H5.9c-.2-.9-.3-1.9-.3-3zM8 14.5c-.8 0-1.6-1.2-2.1-2.5h4.2c-.5 1.3-1.3 2.5-2.1 2.5zm3.6-7h2.8c0 1.1-.2 2.1-.6 3h-2.5c.2-.9.3-1.9.3-3zm.1-1.6c-.2-1.5-.6-2.9-1.1-3.9a6.5 6.5 0 0 1 3.2 3.9z"/></svg>
          <span>LovDryEye.com</span>
        </li>
      </ul>
    </div>
  </section>
</body>
</html>
```